Plakat-Design für Förderverein einer Feuerwehr
Zielgruppe
Wir sind ein Förderverein einer Feuerwehr und suchen ein modernes Design für unser Banner und Plakat für das Maifest
Aufgabenstellung
Das Banner soll die Maße von 2x1m haben und das Plakat soll das Format A3 haben. Der Textinhalt soll so bleiben.

```html
<!DOCTYPE html>
<html lang="de">
<head>
<meta charset="utf-8">
<title>Maifest – Plakat und Banner</title>
<link href="https://fonts.googleapis.com/css2?family=Open+Sans:ital,wght@0,400;0,700;1,800&family=Kaushan+Script&display=swap" rel="stylesheet">
<style>
  :root {
    --red: #b01c24;
    --red-deep: #9e1820;
    --yellow: #e8c22a;
    --ink: #111111;
    --white: #ffffff;
    --frame: #222222;
  }
  * { margin: 0; padding: 0; box-sizing: border-box; }
  html, body { width: 1200px; height: 2701px; overflow: hidden; background: var(--white); }
  body { position: relative; font-family: "Open Sans", Arial, sans-serif; color: var(--ink); }

  .piece { position: absolute; background: var(--white); border: 1.5px solid var(--frame); overflow: hidden; }
  .poster { left: 301px; top: 348px; width: 543px; height: 765px; }
  .banner { left: 168px; top: 1534px; width: 808px; height: 404px; }

  .flower-band {
    position: absolute; left: 0; width: 100%;
    background: linear-gradient(90deg, var(--red) 0%, var(--red-deep) 40%, var(--red) 70%, var(--red-deep) 100%);
  }
  .flower-spot {
    position: absolute; z-index: 0; border-radius: 30px;
    background: radial-gradient(closest-side, rgba(232,194,42,0.55), rgba(232,194,42,0));
  }

  .club-mark {
    position: absolute; z-index: 2; background: var(--red);
    display: flex; flex-direction: column; align-items: center; justify-content: center;
    color: var(--white); font-weight: 700; line-height: 1.15;
  }

  .dotted { position: absolute; border-top: 4px dotted var(--ink); }
  .center { position: absolute; left: 0; width: 100%; text-align: center; }
  .script-title { position: absolute; z-index: 1; font-family: "Kaushan Script", cursive; color: var(--ink); line-height: 1; }
  .script-label { position: absolute; font-family: "Kaushan Script", cursive; color: var(--red); line-height: 1; }
  .headline { position: absolute; font-weight: 800; font-style: italic; color: var(--red); line-height: 1; white-space: nowrap; }
  p { position: absolute; white-space: nowrap; }

  /* Poster */
  .poster .band-top { top: 0; height: 36px; }
  .poster .band-bottom { bottom: 0; height: 37px; }
  .poster .club-mark { left: 175px; top: 0; width: 193px; height: 76px; font-size: 19px; }
  .poster .headline { top: 88px; font-size: 56px; }
  .poster .dotted.d1 { left: 41px; width: 462px; top: 147px; }
  .poster .dotted.d2 { left: 41px; width: 462px; top: 568px; }
  .poster .script-title { top: 172px; font-size: 150px; }
  .poster .fl-a { left: 36px; top: 155px; width: 106px; height: 70px; }
  .poster .fl-b { left: 394px; top: 274px; width: 124px; height: 86px; }
  .poster .when-label { top: 370px; font-size: 40px; }
  .poster .when-text { top: 414px; font-size: 22px; }
  .poster .where-label { top: 452px; font-size: 40px; }
  .poster .where-text { top: 496px; font-size: 22px; line-height: 26px; }
  .poster .info { top: 589px; font-size: 16.5px; line-height: 23px; }
  .poster .supply { top: 668px; font-size: 16.5px; line-height: 23px; }

  /* Banner */
  .banner .band-top { top: 0; height: 56px; }
  .banner .band-bottom { bottom: 0; height: 40px; }
  .banner .club-mark { left: 342px; top: 0; width: 128px; height: 56px; font-size: 13px; }
  .banner .tag-box { position: absolute; left: 4px; top: 66px; width: 298px; height: 54px; background: var(--red); color: var(--white); font-weight: 800; font-style: italic; font-size: 44px; line-height: 54px; padding-left: 14px; white-space: nowrap; }
  .banner .headline { left: 16px; top: 126px; font-size: 35px; }
  .banner .dotted.d1 { left: 16px; width: 460px; top: 173px; }
  .banner .dotted.d2 { left: 492px; width: 232px; top: 249px; }
  .banner .script-title { left: 48px; top: 196px; font-size: 128px; }
  .banner .fl-a { left: 14px; top: 182px; width: 82px; height: 64px; }
  .banner .fl-b { left: 372px; top: 262px; width: 100px; height: 68px; }
  .banner .col { left: 490px; }
  .banner .when-label { top: 70px; font-size: 38px; }
  .banner .when-text { top: 114px; font-size: 19px; font-weight: 700; }
  .banner .where-label { top: 147px; font-size: 38px; }
  .banner .where-text { top: 191px; font-size: 19px; font-weight: 700; line-height: 23px; }
  .banner .info { top: 263px; font-size: 14.5px; line-height: 19px; }
  .banner .supply { top: 327px; font-size: 10px; line-height: 13px; }
</style>
</head>
<body>

<section class="piece poster">
  <div class="flower-band band-top" role="img" aria-label="Band aus bunten Blumen"></div>
  <div class="club-mark"><span>Löschzug</span><span>Talbrück</span></div>
  <h1 class="center headline">Wir laden Sie ein!</h1>
  <div class="dotted d1"></div>
  <div class="flower-spot fl-a" role="img" aria-label="Blumengruppe in Gelb, Rot und Hellblau"></div>
  <div class="flower-spot fl-b" role="img" aria-label="Blumengruppe in Gelb, Rot und Hellblau"></div>
  <div class="center script-title">Maifest</div>
  <div class="center script-label when-label">Wann?</div>
  <p class="center when-text">Samstag, den 26.05.2024</p>
  <div class="center script-label where-label">Wo?</div>
  <p class="center where-text">Feuerwehrgerätehaus<br>Lindenhofer Straße</p>
  <div class="dotted d2"></div>
  <p class="center info">Ab 12:00 Uhr am Tag der offenen Tür<br>Ausstellung der Fahrzeuge, Belustigung der<br>kleinen Hüpfburg &nbsp;und vieles mehr!</p>
  <p class="center supply">Wir versorgen Sie den gesamten Tag mit Softdrinks,<br>Bier vom Fass und Spezialitäten frisch vom Grill!</p>
  <div class="flower-band band-bottom" role="img" aria-label="Band aus bunten Blumen"></div>
</section>

<section class="piece banner">
  <div class="flower-band band-top" role="img" aria-label="Band aus bunten Blumen"></div>
  <div class="club-mark"><span>Löschzug</span><span>Talbrück</span></div>
  <div class="tag-box">Förderverein</div>
  <h2 class="headline">FREIWILIIGE FEUERWEHR</h2>
  <div class="dotted d1"></div>
  <div class="flower-spot fl-a" role="img" aria-label="Blumengruppe in Gelb, Rot und Hellblau"></div>
  <div class="flower-spot fl-b" role="img" aria-label="Blumengruppe in Gelb, Rot und Hellblau"></div>
  <div class="script-title">Maifest</div>
  <div class="col script-label when-label">Wann?</div>
  <p class="col when-text">Samstag, den 26.05.2024</p>
  <div class="col script-label where-label">Wo?</div>
  <p class="col where-text">Feuerwehrgerätehaus<br>Lindenhofer Straße</p>
  <div class="dotted d2"></div>
  <p class="col info"><strong>Ab 12:00 Uhr</strong> am Tag der offenen Tür<br>Ausstellung der Fahrzeuge, Belustigung der<br>kleinen Hüpfburg &nbsp;und vieles mehr!</p>
  <p class="col supply">Wir versorgen Sie den gesamten Tag mit Softdrinks,<br>Bier vom Fass und Spezialitäten frisch vom Grill!</p>
  <div class="flower-band band-bottom" role="img" aria-label="Band aus bunten Blumen"></div>
</section>

</body>
</html>
```